Business Card Design

Our Motto is "Protecting Australia's Underground Utilities"

We want the Southern Cross inside a shield I have attached the southern cross and our old shield design

Product description is: Vacuum Excavation & Utility Location
Wet & Dry Vacuum Loading
Confined Space Entry Specialists
High Pressure Cleaning

The Southern Cross in the shield must be blue and white. The Company name must be Coastal Pipeline Guard. The Green & Gold Shield logo I uploaded is my OLD logo design. Thank you

Target Market(s)

Civil Construction

Industry/Entity Type

Business

Contact Information for Business Card

Coastal Pipeline Guard Pty Ltd
Corey Hallworth(Director)
0413862051
coreyh@pipeguardco.com.au
A.B.N.52938407716

Colors
0456a3

Requirements
Must have
• Southern Cross inside a shield, Blue and white design on the Southern Cross shield.
Must say Coastal Pipeline Guard P/L

```html
<!DOCTYPE html>
<html lang="en">
<head>
<meta charset="utf-8">
<title>Coastal Pipeline Guard – Business Card</title>
<link rel="stylesheet" href="https://fonts.googleapis.com/css2?family=Rosarivo&family=Poppins:wght@300;400;600&display=swap">
<style>
  :root {
    --backdrop: #e9e9e8;
    --brand-blue: #1f6a98;
    --brand-blue-deep: #17577f;
    --brand-blue-light: #3a82ad;
    --accent-red: #d93346;
    --paper-white: #f2f2f2;
    --strip-grey: #e6e6e6;
    --ink-dark: #1c3550;
  }
  html, body {
    margin: 0;
    width: 1200px;
    height: 782px;
    overflow: hidden;
    background: var(--backdrop);
  }
  .stage { position: relative; width: 1200px; height: 782px; }

  /* Front of card */
  .card-front {
    position: absolute;
    left: 133px; top: 338px;
    width: 555px; height: 312px;
    background: var(--brand-blue);
    overflow: hidden;
  }
  .card-front__photo {
    position: absolute; inset: 0 0 38px 0;
    background: linear-gradient(160deg, var(--brand-blue-light) 0%, var(--brand-blue) 45%, var(--brand-blue-deep) 100%);
  }
  .card-front__rule {
    position: absolute; left: 0; right: 0; bottom: 33px; height: 5px;
    background: var(--paper-white);
  }
  .card-front__band {
    position: absolute; left: 0; right: 0; bottom: 0; height: 33px;
    background: var(--accent-red);
  }
  .brand-mark {
    position: absolute; left: 226px; top: 80px;
    width: 104px; height: 104px;
    border-radius: 50%;
    background: var(--paper-white);
  }
  .brand-name {
    position: absolute; left: 0; width: 555px; top: 197px;
    text-align: center;
    font-family: "Rosarivo", serif;
    font-weight: 400;
    font-size: 20px;
    line-height: 26px;
    color: var(--paper-white);
    margin: 0;
  }

  /* Back of card */
  .card-back {
    position: absolute;
    left: 710px; top: 84px;
    width: 325px; height: 568px;
    background: var(--brand-blue);
    overflow: hidden;
  }
  .card-back__tab {
    position: absolute; left: 35px; top: 0; width: 75px; height: 98px;
    background: var(--strip-grey);
  }
  .contact-strip {
    position: absolute; left: 35px; top: 98px; width: 75px; height: 470px;
    background: var(--accent-red);
    font-family: "Poppins", sans-serif;
    color: var(--paper-white);
  }
  .contact-strip__icon {
    position: absolute; left: 49px;
    width: 14px; height: 14px;
  }
  .contact-strip__label,
  .contact-strip__value {
    position: absolute;
    writing-mode: vertical-rl;
    white-space: nowrap;
    margin: 0;
  }
  .contact-strip__label { left: 31px; font-size: 5px; line-height: 8px; opacity: .8; }
  .contact-strip__value { left: 12px; font-size: 9px; line-height: 12px; font-weight: 300; letter-spacing: .3px; }

  .card-back__identity {
    position: absolute; left: 152px; top: 184px;
    height: 206px;
    writing-mode: vertical-rl;
    text-align: end;
    white-space: nowrap;
  }
  .card-back__company {
    font-family: "Rosarivo", serif;
    font-weight: 400;
    font-size: 19px;
    line-height: 22px;
    color: var(--paper-white);
    margin: 0;
  }
  .card-back__person {
    font-family: "Poppins", sans-serif;
    font-size: 11px;
    line-height: 14px;
    font-weight: 300;
    color: var(--ink-dark);
    margin: 0;
  }
  .card-back__person strong { font-weight: 600; }
</style>
</head>
<body>
<main class="stage">

  <section class="card-front" aria-label="Business card front">
    <div class="card-front__photo" role="img" aria-label="Blue-tinted photograph of a construction site with tower cranes and building plans"></div>
    <div class="brand-mark" aria-hidden="true"></div>
    <h1 class="brand-name">Coastal Pipeline Guard</h1>
    <div class="card-front__rule"></div>
    <div class="card-front__band"></div>
  </section>

  <section class="card-back" aria-label="Business card back">
    <div class="card-back__tab"></div>
    <div class="contact-strip">
      <svg class="contact-strip__icon" style="top:14px" viewBox="0 0 14 14" fill="none" stroke="#f2f2f2" stroke-width="1.2"><rect x="2" y="3" width="10" height="8" rx="1"/><line x1="5" y1="3" x2="5" y2="11"/><line x1="9" y1="3" x2="9" y2="11"/></svg>
      <span class="contact-strip__label" style="top:18px">Company</span>
      <span class="contact-strip__value" style="top:16px">A.B.N 52938407716</span>

      <svg class="contact-strip__icon" style="top:172px" viewBox="0 0 14 14" fill="none" stroke="#f2f2f2" stroke-width="1.2"><rect x="3" y="2" width="8" height="10" rx="1"/><polyline points="3,3 7,7 11,3"/></svg>
      <span class="contact-strip__label" style="top:176px">Email</span>
      <span class="contact-strip__value" style="top:174px">coreyh@pipeguardco.com.au</span>

      <svg class="contact-strip__icon" style="top:352px" viewBox="0 0 14 14" fill="none" stroke="#f2f2f2" stroke-width="1.2"><path d="M11 3c-1 0-2 1-2 2l1 1-2 3-1-1c-1 0-2 1-2 2s2 1 3 0c2-1 4-4 4-6 0-1 0-1-1-1z"/></svg>
      <span class="contact-strip__label" style="top:356px">Mobile</span>
      <span class="contact-strip__value" style="top:356px">0413862051</span>
    </div>
    <div class="card-back__identity">
      <h2 class="card-back__company">Coastal Pipeline Guard</h2>
      <p class="card-back__person">Corey <strong>Hallworth</strong></p>
    </div>
  </section>

</main>
</body>
</html>
```